Landing page needed for existing website. High Converting SaaS Landing Page!

Landing page needed for existing website. www.slotnudger.com.au

*Must be designed with Bootstrap framework in mind (so it looks great across all devices).
* Target market is small business owners who take many appointments each day. They want to reduce no shows and remind their customers of appointments dates and times.
* Highlight we intregrate into Plover Diary, Wickham Planner, Or use our Build in Web Calendar
* Competitors (bookvane.com, timeknelltrack.org)
* Clean modern fresh.
* http://quarrylanecreative.com/portfolio_category/web-design/ for inspiration
* Must have link for existing customers to login
* Navigation for future pages.
* Footer section for links to other pages (maybe a contact form)
* The aim of the page is to get prospects to start a Free trial.
* We have 3 domains. slotnudger.com.au (australian customers) slotnudger.co.nz (new zealand customers). slotnudger.info (US customers) these should be linked somewhere. Maybe in the footer with little flags.
Open to ideas on how the page should look. I would prefer something reasonably long with strong imagery.

Target Market(s)

Busy self employer business owners who have many appointments each day. Health professionals, Coaches, Financial Advisers, Tax Lawyers etc etc

Industry/Entity Type

Saas

Number of Pages Required

2 page

Font styles to use
Sans Serif

Requirements
Must have
• 1- Strong Landing Page.
• 2- Stripped down 2nd page that can be used for content, blog posts, content etc.
Nice to have
• Pricing Table

```html
<!DOCTYPE html>
<html lang="en">
<head>
<meta charset="utf-8">
<title>Slot Nudger – Reduce No Shows</title>
<link href="https://fonts.googleapis.com/css2?family=Open+Sans:wght@300;400;600;700&display=swap" rel="stylesheet">
<style>
:root{
  --green:#4fb52f;
  --ink:#2e2e2e;
  --muted:#8a8a8a;
  --light:#f1f1f1;
  --line:#e2e2e2;
  --footer:#2a2a2a;
  --white:#ffffff;
  --badge:#222222;
}
*{box-sizing:border-box;margin:0;padding:0}
html,body{width:1200px;height:2416px;overflow:hidden}
body{font-family:"Open Sans",Arial,sans-serif;color:var(--ink);background:var(--white);position:relative}
section,header,footer{position:absolute;left:0;width:1200px}

/* Hero */
.hero{top:0;height:500px;overflow:hidden}
.hero-media{position:absolute;inset:0;
  background:
    radial-gradient(ellipse 340px 220px at 930px 250px,rgba(235,238,240,.85) 0%,rgba(190,196,200,.55) 45%,rgba(120,110,100,0) 100%),
    radial-gradient(ellipse 260px 180px at 330px 420px,rgba(150,90,50,.55) 0%,rgba(150,90,50,0) 100%),
    radial-gradient(ellipse 300px 160px at 160px 160px,rgba(200,150,90,.35) 0%,rgba(200,150,90,0) 100%),
    linear-gradient(180deg,#2a221c 0%,#4a3a2e 55%,#2a1f18 100%)}
.hero-shade{position:absolute;inset:0;background:linear-gradient(90deg,rgba(0,0,0,.45) 0%,rgba(0,0,0,.1) 55%,rgba(0,0,0,.05) 100%)}
.nav{position:absolute;top:30px;left:0;width:1200px;height:48px}
.brand{position:absolute;left:96px;top:6px;display:flex;align-items:center;gap:10px;color:var(--white);font-weight:700;font-size:22px}
.brand-dot{width:26px;height:26px;border-radius:50%;background:var(--green)}
.menu{position:absolute;left:390px;top:14px;display:flex;gap:40px;list-style:none}
.menu a{color:var(--white);text-decoration:none;font-size:13px;font-weight:600;letter-spacing:.5px;padding-bottom:12px}
.menu a.active{border-bottom:3px solid var(--green)}
.nav-actions{position:absolute;left:920px;top:8px;display:flex;gap:14px}
.btn{display:inline-block;height:34px;line-height:32px;padding:0 18px;font-size:13px;font-weight:600;text-decoration:none;color:var(--white);border-radius:2px}
.btn-outline{border:1px solid var(--white)}
.btn-solid{background:var(--green);border:1px solid var(--green);padding:0 28px}
.hero-title{position:absolute;left:24px;top:190px;color:var(--white);font-size:40px;font-weight:600;line-height:48px;text-shadow:0 2px 6px rgba(0,0,0,.4)}
.hero-badge{position:absolute;left:24px;top:294px;background:var(--green);color:var(--white);font-size:36px;font-weight:700;line-height:52px;padding:0 22px}

/* Booking band */
.booking-band{top:500px;left:160px;width:880px;height:160px;background:var(--green);text-align:center;color:var(--white);box-shadow:0 4px 10px rgba(0,0,0,.12)}
.booking-band h2{font-size:38px;font-weight:400;margin-top:24px;line-height:48px}
.booking-band p{font-size:22px;margin-top:8px;font-weight:300}
.dots{margin-top:10px;display:flex;justify-content:center;gap:8px}
.dots span{width:6px;height:6px;border-radius:50%;background:var(--white)}

/* Calendars */
.calendars{top:700px;height:400px}
.screen{position:absolute;left:64px;top:60px;width:272px;height:178px;border:8px solid #1c1c1c;border-bottom-width:18px;border-radius:6px;background:linear-gradient(135deg,#c9d3db,#7f95a5)}
.screen-stand{position:absolute;left:170px;top:238px;width:60px;height:16px;background:#cfcfcf}
.screen-base{position:absolute;left:146px;top:254px;width:108px;height:6px;background:#bdbdbd;border-radius:3px}
.cal-list{position:absolute;left:440px;top:32px;width:720px;list-style:none}
.cal-item{height:66px;margin-bottom:18px;background:var(--light);display:flex;align-items:center;border-radius:2px}
.cal-name{width:260px;flex:none;display:flex;align-items:center;gap:14px;padding-left:20px;font-size:19px;color:#444;background:var(--white);height:66px;border:1px solid var(--line);white-space:nowrap}
.cal-icon{width:24px;height:24px;border-radius:3px;background:var(--green);flex:none}
.cal-icon.alt{background:#2f6fbf}
.cal-icon.plain{background:none;border:2px solid #555}
.cal-desc{flex:1;padding:0 26px;font-size:11px;line-height:16px;color:var(--muted)}
.cal-desc a{color:#444;text-decoration:none;font-weight:600}

/* Features */
.features{top:1100px;height:500px;background:var(--green);color:var(--white)}
.features h2{text-align:center;font-size:30px;font-weight:400;margin-top:56px}
.divider{position:absolute;left:594px;top:170px;width:12px;height:280px;background:var(--white);border-radius:6px}
.feature{position:absolute;width:520px}
.feature h3{font-size:19px;font-weight:600;margin-bottom:10px}
.feature p{font-size:12px;line-height:18px}
.feature.left{left:40px;text-align:right;padding-right:130px}
.feature.right{left:640px;padding-left:130px}
.f1,.f2{top:168px}.f3,.f4{top:336px}
.badge{position:absolute;top:0;width:100px;height:100px;border-radius:50%;background:var(--badge);display:flex;align-items:center;justify-content:center}
.feature.left .badge{right:0}
.feature.right .badge{left:0}

/* Testimonials */
.testimonials{top:1600px;height:420px;background:var(--white)}
.testimonials h2{text-align:center;font-size:30px;font-weight:400;color:#444;margin-top:60px}
.quote{position:absolute;top:140px;width:500px;height:100px;background:var(--light);padding:20px 28px;font-size:11px;line-height:17px;color:var(--muted);text-align:center}
.quote.q1{left:80px}.quote.q2{left:620px}
.person{position:absolute;top:258px;display:flex;align-items:center;gap:16px}
.person.p1{left:100px}.person.p2{left:640px}
.avatar{width:78px;height:78px;border-radius:50%;background:linear-gradient(135deg,#d9c3ae,#8c7462);border:3px solid var(--white);box-shadow:0 0 0 1px var(--line)}
.person strong{display:block;font-size:13px;color:#444}
.person span{font-size:11px;color:var(--muted)}

/* Footer */
.site-footer{top:2020px;height:396px;background:var(--footer);color:var(--white);text-align:center}
.footer-brand{display:inline-flex;align-items:center;gap:10px;font-size:22px;font-weight:700;margin-top:38px}
.footer-links{margin-top:150px;font-size:13px;letter-spacing:.5px}
.footer-links a{color:var(--white);text-decoration:none}
.copyright{margin-top:10px;font-size:12px;color:#cfcfcf}
.socials{margin-top:36px;display:flex;justify-content:center;gap:18px}
.socials span{width:30px;height:30px;border-radius:50%;background:#4a4a4a}
</style>
</head>
<body>

<section class="hero">
  <div class="hero-media" role="img" aria-label="Photo of a laptop on a café table showing the reminder dashboard"></div>
  <div class="hero-shade"></div>
  <nav class="nav">
    <div class="brand"><span class="brand-dot"></span>Slot Nudger</div>
    <ul class="menu">
      <li><a class="active" href="#">HOME</a></li>
      <li><a href="#">FEATURES</a></li>
      <li><a href="#">PRICING</a></li>
      <li><a href="#">BLOG</a></li>
      <li><a href="#">CONTACT</a></li>
    </ul>
    <div class="nav-actions">
      <a class="btn btn-outline" href="#">Sign Up Free</a>
      <a class="btn btn-solid" href="#">Login</a>
    </div>
  </nav>
  <h1 class="hero-title">Slot Nudger can<br>reduce No Shows</h1>
  <div class="hero-badge">By Up To 90%</div>
</section>

<section class="booking-band">
  <h2>Use Your Favourite Booking Calendar</h2>
  <p>A small software company based</p>
  <div class="dots"><span></span><span></span><span></span></div>
</section>

<section class="calendars">
  <div class="screen" role="img" aria-label="Desktop monitor playing a product video"></div>
  <div class="screen-stand"></div>
  <div class="screen-base"></div>
  <ul class="cal-list">
    <li class="cal-item"><div class="cal-name"><span class="cal-icon"></span>Plover Diary</div>
      <p class="cal-desc">Sync reminders with your diary in real time so every booking gets a timely nudge. <a href="#">Learn more »</a></p></li>
    <li class="cal-item"><div class="cal-name"><span class="cal-icon alt"></span>Wickham Planner</div>
      <p class="cal-desc">Connect your planner once and new appointments are picked up and reminded without effort. <a href="#">Learn more »</a></p></li>
    <li class="cal-item"><div class="cal-name"><span class="cal-icon"></span>Plover Diary</div>
      <p class="cal-desc">Changes and cancellations flow through instantly, keeping each reminder accurate for every client. <a href="#">Learn more »</a></p></li>
    <li class="cal-item"><div class="cal-name"><span class="cal-icon plain"></span>Web Calendar</div>
      <p class="cal-desc">Prefer our built in web calendar? Book, edit and remind clients all from one place. <a href="#">Learn more »</a></p></li>
  </ul>
</section>

<section class="features">
  <h2>Better communication with your customers.</h2>
  <div class="divider"></div>
  <div class="feature left f1">
    <h3>Easy to manage reminders</h3>
    <p>Set up reminders in minutes. Pick a template, choose when it sends, and let the system handle each booking for your clients automatically.</p>
    <div class="badge"><svg width="44" height="44" viewBox="0 0 44 44"><path d="M22 6a12 12 0 0 0-12 12v10l-4 5h32l-4-5V18A12 12 0 0 0 22 6z" fill="none" stroke="#fff" stroke-width="2.5"/><path d="M18 36a4 4 0 0 0 8 0" fill="none" stroke="#fff" stroke-width="2.5"/></svg></div>
  </div>
  <div class="feature right f2">
    <h3>Unlimited scripts</h3>
    <p>Personalise your reminder messages. Unlimited scripts you can use to create the perfect reminder. Mention your customer by name and the key details of their visit.</p>
    <div class="badge"><svg width="44" height="44" viewBox="0 0 44 44"><path d="M8 8h28v20H18l-8 7v-7H8z" fill="none" stroke="#fff" stroke-width="2.5" stroke-linejoin="round"/></svg></div>
  </div>
  <div class="feature left f3">
    <h3>Reply history</h3>
    <p>All SMS, voice and email replies are stored in one log so you can see who confirmed, cancelled or asked to rebook.</p>
    <div class="badge"><svg width="44" height="44" viewBox="0 0 44 44"><circle cx="22" cy="22" r="14" fill="none" stroke="#fff" stroke-width="2.5"/><path d="M22 14v9l6 4" fill="none" stroke="#fff" stroke-width="2.5" stroke-linecap="round"/></svg></div>
  </div>
  <div class="feature right f4">
    <h3>Schedule management</h3>
    <p>Schedule your reminders to go out when you want: 24 hours before, 7 days before, 14 days before, the choice is yours.</p>
    <div class="badge"><svg width="44" height="44" viewBox="0 0 44 44"><rect x="8" y="10" width="28" height="26" rx="2" fill="none" stroke="#fff" stroke-width="2.5"/><path d="M8 18h28M15 6v8M29 6v8" stroke="#fff" stroke-width="2.5"/></svg></div>
  </div>
</section>

<section class="testimonials">
  <h2>Our Testimonials</h2>
  <blockquote class="quote q1">We have saved hours every week since switching. Clients get a friendly text the day before and our empty slots have almost disappeared. The setup took one afternoon.</blockquote>
  <blockquote class="quote q2">Our clinic used to lose several bookings each week. Now patients confirm with a single reply and the front desk spends far less time on the phone chasing.</blockquote>
  <div class="person p1"><div class="avatar" role="img" aria-label="Portrait of Dana Whitlow"></div><div><strong>Dana Whitlow</strong><span>Director Company CEO</span></div></div>
  <div class="person p2"><div class="avatar" role="img" aria-label="Portrait of Priya Castell"></div><div><strong>Priya Castell</strong><span>Director Company CEO</span></div></div>
</section>

<footer class="site-footer">
  <div class="footer-brand"><span class="brand-dot"></span>Slot Nudger</div>
  <p class="footer-links"><a href="#">HOME</a> • <a href="#">SOLUTIONS</a> • <a href="#">SERVICES</a> • <a href="#">COMPANY</a> • <a href="#">CONTACT</a></p>
  <p class="copyright">Copyright © 2017 - 2019 Slot Nudger. Inc. All Rights Reserved</p>
  <div class="socials"><span></span><span></span><span></span><span></span></div>
</footer>

</body>
</html>
```